依頼詳細
グローバルナビ
左サイドメニュー
横幅:960px

今回は、コンペ用のデザイン作成依頼となります。ロゴや電話番号・その他画像データ等サンプルで作成頂ければ幸いです。

《クライアント様からの要望》
すっきりとした見やすいホームページで、患者様やご家族の方に優しい・温かいイメージをもって欲しい。
ロゴに使用されているカラーコードは、「24569d」となります。基調色として取り入れてください。

総合病院で診療科目が多い為、利用者が情報を探しやすいように工夫してください。
病院のPRポイントとしては、「救急患者の受入れを断らない」地域に最先端医療で貢献する。等

(topページに必要なコンテンツ)
・病院からのお知らせ
・はじめてご来院の方へ
-外来受診のご案内
-診療担当・日時
-休診・代診のお知らせ
-入院のご案内
-セカンドオピニオンについて
・お見舞いの皆様へ
・診療科・施設のご案内
-※別途、診療科・施設については添付ファイルを参照ください。
・当院の紹介
・採用情報
・先進医療センター
・周産期医療センター
・消化器病センター
・乳腺診療センター
・地域医療連携への取り組み
サイトURL
ページ数
1ページ
希望イメージ
シンプル 複雑
単色 カラフル
暗い 明るい
日常 高級
遊び心 厳粛
未来的 伝統的
女性的 男性的
希望する色
ブルーを基調(ロゴカラーコード:24569d)差し色はお任せ
納品ファイル
• フォトショップ形式 (.psd)
• PNG形式 (.png)
補足説明
デザインの作成は、Photoshop・Fireworksのみとなります。Illustratorでの作成は不可とします。
(デザイン参考URL)
http://www.tomebara-kouaikai.gr.jp/
http://www.hinokidai.or.jp/
http://kobu.ntmsu.ac.jp/

現サイトのURLにつきましては、個別にメッセージにてお送りさせて頂きますので、希望される方はメッセージをお送りください。
診療科・その他施設一覧ファイルを追加しました。
既存サイトのURLをお伝えした場合、既存サイトのデザインと同じようなご提案が多いため、期間を延長させて頂きます。
既存サイトのURLはお伝えしませんので、斬新なデザインのご提案をお待ちしております。

全体的にスッキリとしている。病院側の伝えたいポイントをしっかりと捉えている。見やすい等、選定理由となりました。

今回、デザイン作成に応募いただきましてありがとうございます。ご提案いただきました全てのデザインをクライアント様に確認いただき、選定させていただきました。
今後とも、機会がありましたら宜しくお願いいたします。

```html
<!DOCTYPE html>
<html lang="ja">
<head>
<meta charset="UTF-8">
<title>サンプル病院</title>
<link href="https://fonts.googleapis.com/css2?family=Noto+Sans+JP:wght@400;700&family=Noto+Serif+JP:wght@700&display=swap" rel="stylesheet">
<style>
:root{
  --brand:#24569d;
  --brand-dark:#1a447f;
  --brand-light:#dfe8f4;
  --accent:#e8789a;
  --accent-light:#fbe3ea;
  --text:#333;
  --muted:#777;
  --line:#d6dce5;
  --bg:#eef1f5;
  --white:#fff;
}
*{box-sizing:border-box;margin:0;padding:0}
html,body{width:720px;height:1200px;overflow:hidden}
body{font-family:"Noto Sans JP",sans-serif;color:var(--text);background:var(--bg);font-size:10px;position:relative}
ul{list-style:none}
a{color:inherit;text-decoration:none}

.site-header{height:70px;background:var(--white);position:relative}
.logo{position:absolute;left:30px;top:18px;display:flex;align-items:center;gap:8px}
.logo-mark{width:28px;height:28px;background:var(--brand)}
.logo-sub{font-size:9px;color:var(--muted);display:block}
.logo-name{font-size:16px;font-weight:700;color:var(--brand);line-height:1.1}
.search{position:absolute;right:30px;top:12px;display:flex}
.search span{width:120px;height:16px;border:1px solid var(--line)}
.search b{width:34px;height:16px;background:var(--brand);color:#fff;font-size:8px;text-align:center;line-height:16px;font-weight:400}
.utility{position:absolute;right:30px;top:38px;display:flex;gap:14px;font-size:9px;color:var(--brand)}
.utility li::before{content:"";display:inline-block;width:6px;height:6px;background:var(--brand);border-radius:50%;margin-right:4px}

.global-nav{height:36px;background:linear-gradient(#3a6db4,var(--brand-dark));display:flex;padding:0 24px}
.global-nav li{flex:1;color:#fff;font-size:10.5px;text-align:center;line-height:36px;border-right:1px solid rgba(255,255,255,.3)}
.global-nav li:first-child{border-left:1px solid rgba(255,255,255,.3)}

.hero{height:182px;background:linear-gradient(90deg,#fff 0%,#f4f8fc 50%,#dfe9f5 100%);position:relative}
.hero-copy{position:absolute;left:44px;top:38px}
.hero-copy .lead{font-family:"Noto Serif JP",serif;font-size:22px;color:var(--brand);font-weight:700}
.hero-copy h1{font-family:"Noto Serif JP",serif;font-size:34px;color:var(--brand);letter-spacing:2px;line-height:1.2}
.hero-copy p{font-size:10px;color:var(--muted);margin-top:10px;line-height:1.6}
.hero-photo{position:absolute;right:0;top:0;width:360px;height:182px;background:linear-gradient(120deg,#f7fafd,#c9d9ec 60%,#aec6e2)}

.first-visit{padding:0 24px;position:relative}
.first-visit .tab{display:inline-block;background:var(--accent);color:#fff;font-size:10px;padding:3px 14px;margin-top:-10px;position:relative}
.first-visit ul{display:flex;gap:6px;margin-top:6px}
.first-visit li{flex:1;height:34px;background:var(--white);border:1px solid var(--line);display:flex;align-items:center;gap:6px;padding-left:10px;font-size:10px;color:var(--brand)}
.first-visit li i{width:16px;height:16px;border-radius:50%;background:var(--brand-light);border:2px solid var(--brand)}

.content{display:flex;gap:14px;padding:0 24px;margin-top:26px}
.main{width:528px;background:var(--white);border:1px solid var(--line);padding:12px}
.sidebar{width:130px}

.section-title{background:var(--brand);color:#fff;font-size:11px;font-weight:700;padding:5px 10px;display:flex;justify-content:space-between}
.section-title small{font-size:8px;font-weight:400;border:1px solid #fff;padding:0 6px}

.departments{display:flex;gap:10px;margin-top:14px}
.dept{flex:1}
.dept h3{font-size:12px;color:var(--brand);border-bottom:2px solid var(--brand);padding:2px 4px}
.dept .thumb{height:34px;margin:6px 0;background:linear-gradient(90deg,#eef3f9,#c6d6ea)}
.dept li{font-size:9.5px;line-height:16px;color:var(--brand)}
.dept li::before{content:"▸ ";color:var(--accent)}

.centers{margin-top:24px;border:1px solid var(--line)}
.centers h3{background:var(--brand-light);color:var(--brand);font-size:11px;padding:5px 10px}
.centers ul{display:grid;grid-template-columns:1fr 1fr;padding:6px 12px}
.centers li{font-size:9.5px;line-height:24px;border-bottom:1px dotted var(--line);color:var(--brand);margin-right:14px}
.centers li::before{content:"▸ ";color:var(--accent)}

.news{margin-top:24px}
.news li{font-size:9.5px;line-height:24px;border-bottom:1px dotted var(--line);padding-left:8px}
.news time{color:var(--muted);margin-right:16px}
.news a{color:var(--brand)}

.side-menu li{background:var(--white);border:1px solid var(--line);border-left:4px solid var(--brand);font-size:10px;padding:6px 8px;margin-bottom:4px;color:var(--brand)}
.side-btn{display:block;background:var(--accent);color:#fff;font-size:10px;padding:7px 8px;margin:14px 0}
.side-links li{display:flex;align-items:center;gap:6px;background:var(--white);border:1px solid var(--line);padding:5px;margin-bottom:6px;font-size:9.5px;color:var(--brand)}
.side-links .thumb{width:40px;height:36px;background:linear-gradient(#e3ecf6,#b9cde5);flex:none}

.site-footer{position:absolute;left:0;top:1084px;width:720px}
.footer-links{display:flex;gap:16px;padding:0 24px 10px;font-size:9px;color:var(--brand)}
.copyright{background:var(--brand);color:#fff;font-size:8.5px;text-align:right;padding:7px 24px}
</style>
</head>
<body>
<header class="site-header">
  <div class="logo">
    <span class="logo-mark"></span>
    <div><span class="logo-sub">医療法人</span><span class="logo-name">サンプル病院</span></div>
  </div>
  <div class="search"><span></span><b>検索</b></div>
  <ul class="utility"><li>ホーム</li><li>サイトマップ</li><li>文字サイズ変更</li></ul>
</header>

<nav class="global-nav">
  <ul style="display:flex;width:100%">
    <li>当院のご紹介</li><li>診療科のご案内</li><li>施設のご案内</li><li>お見舞いの皆様へ</li><li>交通アクセス</li>
  </ul>
</nav>

<section class="hero">
  <div class="hero-copy">
    <p class="lead">地域に貢献する</p>
    <h1>最先端医療</h1>
    <p>救急患者の受入れを断らない。<br>患者様とご家族に寄り添う医療を提供します。</p>
  </div>
  <div class="hero-photo" role="img" aria-label="白衣の医師と看護師の写真"></div>
</section>

<section class="first-visit">
  <span class="tab">初めてご来院の方へ</span>
  <ul>
    <li><i></i>外来受診のご案内</li>
    <li><i></i>診療担当・日時</li>
    <li><i></i>休診・代診のお知らせ</li>
    <li><i></i>入院のご案内</li>
    <li><i></i>セカンドオピニオン</li>
  </ul>
</section>

<div class="content">
  <main class="main">
    <h2 class="section-title">診療科のご案内</h2>
    <div class="departments">
      <div class="dept">
        <h3>内 科</h3>
        <div class="thumb" role="img" aria-label="内科の診察風景の写真"></div>
        <ul><li>総合内科・呼吸器内科</li><li>循環器内科</li><li>消化器内科</li><li>神経内科</li><li>腎臓内科</li><li>代謝内分泌内科</li><li>血液内科</li><li>小児科</li></ul>
      </div>
      <div class="dept">
        <h3>外 科</h3>
        <div class="thumb" role="img" aria-label="外科の手術室の写真"></div>
        <ul><li>一般外科</li><li>脳神経外科</li><li>心臓血管外科</li><li>呼吸器外科</li><li>整形外科</li><li>形成外科</li><li>泌尿器科</li></ul>
      </div>
      <div class="dept">
        <h3>救急科</h3>
        <div class="thumb" role="img" aria-label="救急外来の写真"></div>
        <ul><li>救急科</li><li>麻酔科</li><li>放射線科</li><li>病理診断科</li></ul>
      </div>
    </div>

    <section class="centers">
      <h3>診療・施設案内</h3>
      <ul>
        <li>先進医療センター</li><li>周産期医療センター</li>
        <li>消化器病センター</li><li>乳腺診療センター</li>
        <li>健診センター</li><li>透析センター</li>
        <li>リハビリテーション室</li><li>薬剤部</li>
        <li>地域医療連携室</li><li>栄養管理室</li>
      </ul>
    </section>

    <section class="news">
      <h2 class="section-title">病院からのお知らせ <small>一覧を見る</small></h2>
      <ul>
        <li><time>2013/05/21</time><a>外来診療の受付時間変更についてのお知らせです</a></li>
        <li><time>2013/05/18</time><a>市民公開講座の開催についてのお知らせです</a></li>
        <li><time>2013/05/15</time><a>休診・代診の予定を更新しました</a></li>
        <li><time>2013/05/10</time><a>採用情報を更新しました</a></li>
        <li><time>2013/05/02</time><a>連休中の診療体制についてのお知らせです</a></li>
      </ul>
    </section>
  </main>

  <aside class="sidebar">
    <ul class="side-menu">
      <li>内科</li><li>外科</li><li>救急科</li><li>地域医療連携のご案内</li>
    </ul>
    <a class="side-btn">初めてご来院の方へ</a>
    <ul class="side-links">
      <li><span class="thumb" role="img" aria-label="電車の写真"></span>交通アクセス</li>
      <li><span class="thumb" role="img" aria-label="花の写真"></span>お見舞いの皆様へ</li>
      <li><span class="thumb" role="img" aria-label="職員の写真"></span>採用情報</li>
      <li><span class="thumb" role="img" aria-label="街並みの写真"></span>地域医療連携の取り組み</li>
    </ul>
  </aside>
</div>

<footer class="site-footer">
  <ul class="footer-links"><li>HOME</li><li>サイトマップ</li><li>プライバシーポリシー</li><li>お問い合わせ</li></ul>
  <p class="copyright">Copyright © サンプル病院 All Rights Reserved.</p>
</footer>
</body>
</html>
```